Business card design needed

I need a business card for my private practice. I would like to see the designs that use bright blue and white. I would like to see similar designs as to the card below:
http://blog.printvarno.com/2009/designing-a-business-card-with-pv-ks517-template.html
I would like to see the back of the card have room for appointment times. Thank you.

Industry/Entity Type
Business
Contact Information for Business Card
Brightwater Counselling & Wellness Services
Helen Dorsey B.Psychology
Registered Psychologist
Building C, Level 3, 14 Marrow Crescent, Canberra, ACT 2601
T: (02) 6287 5912
F: (02) 6287 5930
info@brightwatercounselling.com.au
www.brightwatercounselling.com.au

```html
<!DOCTYPE html>
<html lang="en">
<head>
<meta charset="utf-8">
<title>Brightwater Counselling &amp; Wellness Services – Business Card</title>
<link rel="stylesheet" href="https://fonts.googleapis.com/css2?family=Arimo:wght@400;700&family=PT+Sans:wght@400;700&display=swap">
<style>
  :root {
    --navy: #27446a;
    --sky: #3a9ad9;
    --card-top: #f3f5f9;
    --card-bottom: #e6ebf3;
    --paper: #ffffff;
    --ink: #2d4568;
    --backdrop: #dfe2e7;
  }
  * { box-sizing: border-box; margin: 0; padding: 0; }
  html, body {
    width: 1200px; height: 1000px; overflow: hidden;
    background: var(--backdrop);
  }
  .stage { position: relative; width: 1200px; height: 1000px; }

  /* Front of card */
  .card-front {
    position: absolute; left: 184px; top: 47px; width: 793px; height: 435px;
    background: linear-gradient(var(--card-top), var(--card-bottom));
    overflow: hidden;
    box-shadow: 0 3px 8px rgba(0,0,0,.25);
  }
  .card-front .side-panel { position: absolute; left: 0; top: 0; width: 400px; height: 435px; }
  .card-front .top-rule {
    position: absolute; left: 351px; top: 0; right: 0; height: 6px; background: var(--sky);
  }
  .card-front .bottom-rule {
    position: absolute; left: 346px; bottom: 0; right: 0; height: 8px; background: var(--navy);
  }
  .website {
    position: absolute; right: 15px; top: 17px;
    font: 400 16px/1 "PT Sans", sans-serif; letter-spacing: .6px; color: var(--ink);
    text-transform: uppercase;
  }
  .practice-name {
    position: absolute; left: 86px; top: 158px;
    font: 400 16.5px/1 "Arimo", sans-serif; letter-spacing: .5px; color: var(--ink);
    text-transform: uppercase; white-space: nowrap;
  }
  .practice-name strong { font-weight: 700; }
  .person { position: absolute; left: 454px; top: 251px; }
  .person-name {
    font: 700 27px/1 "PT Sans", sans-serif; color: var(--ink); letter-spacing: .3px;
    text-transform: uppercase;
  }
  .person-title {
    margin-top: 1px; padding-left: 28px;
    font: 400 12px/1 "PT Sans", sans-serif; color: var(--sky); text-transform: uppercase; letter-spacing: .3px;
  }
  .contact {
    position: absolute; left: 454px; top: 310px;
    font: 400 14px/17px "PT Sans", sans-serif; color: var(--ink); letter-spacing: .5px;
    text-transform: uppercase; list-style: none;
  }
  .contact .label { display: inline-block; width: 28px; text-align: right; padding-right: 4px; color: var(--sky); font-weight: 700; }

  /* Back of card */
  .card-back {
    position: absolute; left: 184px; top: 521px; width: 791px; height: 432px;
    background: linear-gradient(var(--card-top), var(--card-bottom));
    box-shadow: 0 3px 8px rgba(0,0,0,.25);
    overflow: hidden;
  }
  .card-back .heading {
    position: absolute; left: 0; right: 0; top: 18px; text-align: center;
    font: 700 20px/1 "Arimo", sans-serif; color: var(--ink); letter-spacing: .4px;
  }
  .appointment-box {
    position: absolute; left: 11px; top: 66px; width: 770px; height: 350px;
    background: var(--paper);
  }
  .card-back .bottom-rule { position: absolute; left: 0; right: 0; bottom: 0; height: 9px; background: var(--navy); }
  .slot-column { position: absolute; top: 10px; width: 270px; list-style: none; }
  .slot-column.first { left: 48px; }
  .slot-column.second { left: 446px; }
  .column-title {
    display: block; text-align: center; margin-bottom: 9px;
    font: 400 16px/1 "Arimo", sans-serif; color: var(--ink); padding-left: 2px;
  }
  .slot {
    display: flex; align-items: flex-end; height: 40px;
    font: 700 14px/1 "Arimo", sans-serif; color: var(--ink); letter-spacing: 1px;
  }
  .slot:first-of-type { height: 30px; }
  .slot .num { width: 28px; text-align: right; }
  .slot .line { flex: 0 0 246px; margin-left: 2px; border-bottom: 1.5px dashed var(--ink); height: 1px; margin-bottom: 1px; }
</style>
</head>
<body>
<main class="stage">

  <section class="card-front" aria-label="Business card front">
    <svg class="side-panel" viewBox="0 0 400 435" aria-hidden="true">
      <path d="M0,0 H335 C130,45 20,140 20,218 C20,300 125,392 345,435 H0 Z" fill="var(--navy)"/>
    </svg>
    <div class="top-rule"></div>
    <div class="bottom-rule"></div>

    <p class="website">www.brightwatercounselling.com.au</p>
    <h1 class="practice-name"><strong>Brightwater Counselling</strong> &amp; Wellness Services</h1>

    <div class="person">
      <h2 class="person-name">Helen Dorsey</h2>
      <p class="person-title">Registered Psychologist</p>
    </div>

    <ul class="contact">
      <li>Building C, Level 3, 14 Marrow Crescent,</li>
      <li>Canberra ACT 2601</li>
      <li><span class="label">T:</span>(02) 6287 5912</li>
      <li><span class="label">F:</span>(02) 6287 5930</li>
      <li><span class="label">E:</span>info@brightwatercounselling.com.au</li>
    </ul>
  </section>

  <section class="card-back" aria-label="Business card back">
    <h2 class="heading">Your next appointment times</h2>
    <div class="appointment-box">
      <ol class="slot-column first">
        <li class="column-title">Date &amp; time</li>
        <li class="slot"><span class="num">1.</span><span class="line"></span></li>
        <li class="slot"><span class="num">2.</span><span class="line"></span></li>
        <li class="slot"><span class="num">3.</span><span class="line"></span></li>
        <li class="slot"><span class="num">4.</span><span class="line"></span></li>
        <li class="slot"><span class="num">5.</span><span class="line"></span></li>
        <li class="slot"><span class="num">6.</span><span class="line"></span></li>
        <li class="slot"><span class="num">7.</span><span class="line"></span></li>
      </ol>
      <ol class="slot-column second">
        <li class="column-title">Date &amp; time</li>
        <li class="slot"><span class="num">8.</span><span class="line"></span></li>
        <li class="slot"><span class="num">9.</span><span class="line"></span></li>
        <li class="slot"><span class="num">10.</span><span class="line"></span></li>
        <li class="slot"><span class="num">11.</span><span class="line"></span></li>
        <li class="slot"><span class="num">12.</span><span class="line"></span></li>
        <li class="slot"><span class="num">13.</span><span class="line"></span></li>
        <li class="slot"><span class="num">14.</span><span class="line"></span></li>
      </ol>
    </div>
    <div class="bottom-rule"></div>
  </section>

</main>
</body>
</html>
```